design a construction company business card

Design business card around our logo. Card must have all the typical info: name, title, address, phone, email, business name, etc. Somewhere on the card I would like to see our motto "Built on integrity... Inspired by commitment." Consider adding a splash of bright orange to the card to complement the blues and silvers/grays in the logo. We are open to metallic inks, textures, etc. We would like to see options on both light and dark backgrounds. The font in the logo is Euro Technic Extended Regular.

```html
<!DOCTYPE html>
<html lang="en">
<head>
<meta charset="utf-8">
<title>Halden Contracting business card</title>
<link href="https://fonts.googleapis.com/css2?family=Montserrat:wght@400;500;600&display=swap" rel="stylesheet">
<style>
  :root {
    --backdrop: #2a2a2c;
    --card: #1c1c1e;
    --blue: #2f78d2;
    --orange: #f07f1e;
    --grey: #c9c9cc;
    --gold: #c8b772;
    --gold-light: #ddd09a;
    --silver: #c4c4c6;
  }
  * { box-sizing: border-box; margin: 0; padding: 0; }
  html, body { width: 1200px; height: 814px; overflow: hidden; }
  body {
    background: var(--backdrop);
    font-family: "Montserrat", sans-serif;
    position: relative;
  }
  .card {
    position: absolute;
    top: 252px;
    width: 540px;
    height: 309px;
    background: var(--card);
    border-radius: 4px;
    box-shadow: 0 10px 30px rgba(0,0,0,.45);
    overflow: hidden;
  }
  .card-front { left: 40px; }
  .card-back { left: 620px; }

  .person { position: absolute; left: 42px; top: 40px; }
  .person-name { color: var(--blue); font-size: 22px; font-weight: 500; letter-spacing: 1px; text-transform: uppercase; }
  .person-title { color: var(--grey); font-size: 14px; font-weight: 400; margin-top: 2px; }

  .contact { position: absolute; left: 42px; top: 112px; list-style: none; }
  .contact li { color: var(--grey); font-size: 12px; display: flex; align-items: center; gap: 9px; height: 19px; }
  .contact svg { width: 11px; height: 11px; fill: var(--blue); }

  .company { position: absolute; right: 40px; top: 58px; text-align: right; }
  .company-name { color: var(--blue); font-size: 40px; font-weight: 600; letter-spacing: 3px; line-height: 1; }
  .company-sub { color: var(--blue); font-size: 11px; font-weight: 600; letter-spacing: 2px; margin-top: 6px; }

  .accent-line { position: absolute; left: 0; right: 0; top: 202px; height: 2px; background: var(--orange); }

  .address {
    position: absolute; right: 40px; top: 228px;
    color: var(--grey); font-size: 12px; font-style: normal;
    line-height: 1.45; text-align: right;
  }

  .motto {
    position: absolute;
    left: 40px;
    top: 275px;
    transform: rotate(-90deg);
    transform-origin: left top;
    color: var(--orange);
    font-size: 17px;
    line-height: 1.45;
    white-space: nowrap;
  }
  .foil-area {
    position: absolute;
    left: 150px;
    top: 22px;
    right: 0;
    bottom: 20px;
    background: linear-gradient(160deg, var(--gold) 0%, var(--gold-light) 45%, var(--silver) 70%, var(--gold) 100%);
  }
</style>
</head>
<body>
  <section class="card card-front">
    <div class="person">
      <h1 class="person-name">Alex Morgan</h1>
      <p class="person-title">Manager</p>
    </div>
    <ul class="contact">
      <li><svg viewBox="0 0 12 12"><path d="M2 1h3l1 3-2 1a7 7 0 0 0 3 3l1-2 3 1v3c-6 0-9-3-9-9z"/></svg>555-014-2288</li>
      <li><svg viewBox="0 0 12 12"><path d="M1 2h10v8H1zM1.5 2.5 6 6.5l4.5-4" stroke="#1c1c1e" stroke-width="1"/></svg>alex.morgan@halden.com</li>
      <li><svg viewBox="0 0 12 12"><circle cx="6" cy="6" r="5.5"/></svg>www.halden.com</li>
    </ul>
    <div class="company">
      <p class="company-name">HALDEN</p>
      <p class="company-sub">CONTRACTING, INC.</p>
    </div>
    <div class="accent-line"></div>
    <address class="address">48 Cedar Row<br>Millbrook, AB, T2B 4K7</address>
  </section>

  <section class="card card-back">
    <p class="motto">Built on integrity...<br>Inspired by commitment</p>
    <div class="foil-area" role="img" aria-label="Gold and silver metallic foil decoration"></div>
  </section>
</body>
</html>
```